Home page makeover

Take my existing home page, www.maplecrestledger.com and redesign layout to look more current considering today's touch design prevalence.
Reuse existing elements or suggest improved ones if available.
I generally have average CSS and HTML skills using div containers, defining lists and using columns to create the code to support the layout.
Updates
Just wanted to send out a quick message to thank all of you for your submissions. Many of you offered nice designs, but unfortunately could only choose one.
Target Market(s)
Generally targeting individuals with some assets for retirement. Basically your average working professional or business owner.
Industry/Entity Type
It Support
Look and feel
Each slider illustrates characteristics of the customer's brand and the style your logo design should communicate.

```html
<!DOCTYPE html>
<html lang="en">
<head>
<meta charset="utf-8">
<title>Maplecrest Ledger — Home</title>
<link rel="stylesheet" href="https://fonts.googleapis.com/css2?family=Roboto:ital,wght@0,400;0,500;0,700;0,900;1,300;1,400&display=swap">
<style>
:root{
  --green:#1e6b2a;
  --green-band:#1f6a2b;
  --green-dark:#0f3f17;
  --ink:#333;
  --grey-text:#666;
  --btn-grey:#444;
  --footer:#2b2b2b;
  --footer-line:#4a4a4a;
  --white:#fff;
}
*{margin:0;padding:0;box-sizing:border-box}
html,body{width:1200px;height:900px;overflow:hidden;background:var(--white);font-family:'Roboto',sans-serif}
.page{position:relative;width:1200px;height:900px}

/* header */
.site-header{position:absolute;top:0;left:0;width:1200px;height:84px;border-bottom:4px solid #1a1a1a;background:var(--white)}
.brand{position:absolute;left:296px;top:18px;display:flex;align-items:center;gap:10px}
.brand-mark{width:36px;height:36px;background:var(--green)}
.brand-name{font-size:27px;font-weight:500;color:var(--green);letter-spacing:.2px}
.account-links{position:absolute;left:732px;top:0;width:83px;height:18px;background:var(--green-dark);color:var(--white);font-size:9px;line-height:16px;text-align:center}
.tagline{position:absolute;left:820px;top:12px;display:flex;align-items:center;gap:8px}
.tagline-mark{width:36px;height:36px;border-radius:50%;background:#e6e6e6}
.tagline-text{font-size:14px;font-weight:400;line-height:17px;color:var(--ink)}
.main-nav{position:absolute;left:562px;top:54px;display:flex;height:27px}
.main-nav a{font-size:11px;color:var(--green);text-decoration:none;line-height:28px;margin-left:20px;white-space:nowrap}
.main-nav a.active{background:var(--green);color:var(--white);padding:0 9px;margin-left:0}

/* hero */
.hero{position:absolute;top:84px;left:0;width:1200px;height:297px;background:var(--green-band)}
.video{position:absolute;left:296px;top:24px;width:349px;height:241px;background:#000}
.video-title{position:absolute;left:8px;top:4px;font-size:9px;color:#ddd}
.video-still{position:absolute;left:43px;top:21px;width:264px;height:197px;background:linear-gradient(135deg,#e8e8e8,#8a8a8a 60%,#3a3a3a)}
.play{position:absolute;left:147px;top:100px;width:56px;height:38px}
.video-bar{position:absolute;left:0;bottom:0;width:349px;height:22px;background:#1b1b1b}
.video-bar .track{position:absolute;left:0;top:-3px;width:349px;height:3px;background:#555}
.video-bar .time{position:absolute;left:60px;top:6px;font-size:8px;color:#ccc}
.signup{position:absolute;left:672px;top:72px;width:248px;color:var(--white)}
.signup h1{padding-left:8px;font-size:56px;font-weight:900;line-height:64px;text-shadow:2px 3px 3px rgba(0,0,0,.45);white-space:nowrap}
.signup p{font-size:13px;font-style:italic;font-weight:300;text-align:center;line-height:20px;white-space:nowrap}
.signup strong{font-style:normal;font-weight:700;font-size:17px}
.pointer{position:absolute;left:752px;top:222px;width:80px;height:75px;background:linear-gradient(180deg,rgba(255,255,255,.15),rgba(255,255,255,.85))}

/* features */
.features{position:absolute;top:420px;left:0;width:1200px}
.feature{position:absolute;width:200px;text-align:center}
.feature-icon{margin:0 auto;width:86px;height:86px;border-radius:50%;background:var(--green);border:3px solid var(--white);box-shadow:6px 6px 5px rgba(0,0,0,.3);display:flex;align-items:center;justify-content:center}
.feature h2{margin-top:37px;font-size:16px;font-weight:700;color:var(--green)}
.feature p{margin-top:11px;font-size:10px;line-height:16.3px;color:var(--grey-text);padding:0 6px}
.feature .details{display:inline-block;margin-top:29px;background:var(--btn-grey);color:var(--white);font-size:8.5px;padding:3px 5px;text-decoration:none}

/* footer */
.site-footer{position:absolute;top:744px;left:0;width:1200px;height:156px;background:var(--footer)}
.footer-links{position:absolute;top:24px;list-style:none}
.footer-links li{width:107px;height:20.2px;border-bottom:1px solid var(--footer-line);font-size:8.5px;color:var(--white);line-height:17px;padding-left:20px}
.newsletter{position:absolute;left:682px;top:34px;display:flex}
.newsletter span{width:205px;height:23px;background:var(--white);font-size:8.5px;color:#333;line-height:23px;padding-left:15px}
.newsletter b{width:25px;height:23px;background:var(--green);display:flex;align-items:center;justify-content:center}
.social{position:absolute;left:836px;top:89px;display:flex;gap:6px}
.social i{width:24px;height:24px;border-radius:50%;background:#e8e0c8;border:2px solid #555}
.copyright{position:absolute;left:684px;top:139px;font-size:8.5px;color:var(--white)}
</style>
</head>
<body>
<div class="page">
  <header class="site-header">
    <div class="brand"><span class="brand-mark"></span><span class="brand-name">Maplecrest Ledger</span></div>
    <div class="account-links">Sign Up &nbsp;|&nbsp; Sign In</div>
    <div class="tagline"><span class="tagline-mark"></span><span class="tagline-text">It's<br>Your<br>Tomorrow</span></div>
    <nav class="main-nav">
      <a class="active" href="#">HOME</a><a href="#">ABOUT US</a><a href="#">SERVICES</a><a href="#">CONTACT US</a>
    </nav>
  </header>

  <section class="hero">
    <div class="video">
      <span class="video-title">Demo.wmv</span>
      <div class="video-still" role="img" aria-label="Video still of a laptop keyboard with reading glasses and the word Plan"></div>
      <svg class="play" viewBox="0 0 56 38"><rect width="56" height="38" rx="8" fill="#222"/><path d="M23 12 L35 19 L23 26Z" fill="#fff"/></svg>
      <div class="video-bar"><span class="track"></span>
        <svg style="position:absolute;left:12px;top:6px" width="10" height="10"><path d="M1 0 L9 5 L1 10Z" fill="#aaa"/></svg>
        <span class="time">0:00 / 0:28</span>
      </div>
    </div>
    <div class="signup">
      <h1>SIGN UP</h1>
      <p>Only <strong>$19.99</strong> For a One Year Membership<br>Only <strong>$9.99</strong> Per Year After That</p>
    </div>
    <div class="pointer" role="img" aria-label="Illustration of a white hand pointing up toward the sign up offer"></div>
  </section>

  <section class="features">
    <div class="feature" style="left:293px">
      <div class="feature-icon"><svg width="32" height="24" viewBox="0 0 32 24" fill="none" stroke="#fff" stroke-width="2"><rect x="1" y="1" width="30" height="22"/><rect x="5" y="6" width="8" height="10"/><path d="M16 8h11M16 12h11M16 16h8"/></svg></div>
      <h2>IDENTIFY</h2>
      <p>Identify and project your retirement needs and expectations including basic living expenses, housing costs, recreation, big ticket non-recurring items, medical and nursing home care</p>
      <a class="details" href="#">+ View Details</a>
    </div>
    <div class="feature" style="left:517px">
      <div class="feature-icon"><svg width="30" height="24" viewBox="0 0 30 24" fill="none" stroke="#fff" stroke-width="2"><path d="M1 4 L10 1 L20 4 L29 1 V20 L20 23 L10 20 L1 23Z"/><path d="M7 15 L13 10 L18 13 L24 7"/></svg></div>
      <h2>PLAN</h2>
      <p>Identify and project your retirement needs and expectations including basic living expenses, housing costs, recreation, big ticket non-recurring items, medical and nursing home care</p>
      <a class="details" href="#">+ View Details</a>
    </div>
    <div class="feature" style="left:735px">
      <div class="feature-icon"><svg width="32" height="28" viewBox="0 0 32 28" fill="none" stroke="#fff" stroke-width="2"><path d="M2 8 L10 14 M30 8 L22 14 M10 14 L16 20 L22 14 M12 11 L18 8 L22 14"/></svg></div>
      <h2>RETIRE</h2>
      <p>Identify and project your retirement needs and expectations including basic living expenses, housing costs, recreation, big ticket non-recurring items, medical and nursing home care</p>
      <a class="details" href="#">+ View Details</a>
    </div>
  </section>

  <footer class="site-footer">
    <ul class="footer-links" style="left:313px">
      <li>HOME</li><li>ABOUT US</li><li>SERVICES</li><li>CONTACT US</li><li>&nbsp;SIGN IN</li><li>SIGN UP</li>
    </ul>
    <ul class="footer-links" style="left:494px">
      <li>&nbsp;FEATURES</li><li>&nbsp;TESTIMONIALS</li><li>&nbsp;FAQ</li><li>&nbsp;PRIVACY &amp; POLICY</li><li>&nbsp;SITE MAP</li>
    </ul>
    <div class="newsletter"><span>Newsleter Sign Up</span><b><svg width="10" height="12" viewBox="0 0 10 12"><path d="M2 1 L8 6 L2 11" fill="none" stroke="#fff" stroke-width="2.5"/></svg></b></div>
    <div class="social"><i></i><i></i><i></i></div>
    <p class="copyright">Copyright (C) &nbsp;maplecrestledger.com. All Rights Reserved</p>
  </footer>
</div>
</body>
</html>
```